Website for Vorentix - A Leader in AI (artificial Intelligence), Metaverse, Blockchain, and Web3

Project Description:
We are looking for a talented web designer to create a comprehensive website for Vorentix, a cutting-edge company specializing in the AI & metaverse, blockchain, and Web3 technologies. The website will serve as a digital portal to showcase our services, solutions, and insights into the digital landscape. We aim to provide an immersive user experience that reflects our identity and expertise in the field.
You will be provided with:
Vorentix’s logo and branding materials to ensure consistency with our visual identity.
Colors Palate
Bright Sky Blue #18DEFF
White #FFFFFF
Vivid Cerulean #52B8FF
Light Lavender #B07CFF
#000000
Typography Montserrat
Detailed Scope of Work:
1. Home Page
URL: /
Purpose: Establish Vorentix’s identity and encourage exploration of services and insights.
Key Sections:
Hero Banner:
Main Headline: “Building the Future of the Metaverse & Web3”
Short Description: Highlight Vorentix as innovators in AI, ML, AR, VR, MR, IoT.
Call to Action: Links to “About Vorentix,” “Services,” and “Build an Avatar.”
Focus Areas:
Quick mentions of immersive environments, blockchain projects, and AI integration.
Child companies Section plovmark and the amber quill and 2 CTA to lead to dedicated page and the other cta directly to website
Why Choose Vorentix:
List of bullet points highlighting expertise and unique strategies.
Featured Projects:
Teasers of significant achievements like metaverse real estate.
Final Call to Action:
Links to more detailed service pages.
2. About Us
URL: /about
Purpose: Provide detailed background and showcase technological passion.
Key Sections:
Who Is Vorentix, Tech Expertise, Our Vision, Why Businesses Need Vorentix, Our Fantastic Journey, Our Metaverse Expertise, Our Team & Organizational Chart.
3. Vorentix Guides
URL: /vorentix-guides
Purpose: Offer technical and business insights into metaverse and blockchain.
Key Sections: Intro, Popular Articles, Technical Deep-Dives.
4. Privacy Policy
URL: /privacy
Purpose: Detail data handling practices in compliance with regulations.
Key Sections: Data Types Collected, Usage, Cookies, User Rights, Data Retention, Privacy Contacts.
5. Support
URL: /support
Purpose: Central hub for customer and technical support.
Key Sections: Contact Methods, Troubleshooting, Documentation, Response Times.
6. Community Rules
URL: /community-rules
Purpose: Set guidelines for interaction within community platforms.
Key Sections: Conduct, Prohibited Content, Reporting, Moderation, Consequences.
7. Build an Avatar
URL: /build-an-avatar
Purpose: Guide for creating 3D avatars in Vorentix’s metaverse.
Key Sections: Introduction, Creation Steps, Integration, Avatar FAQs.
8. Terms of Service
URL: /terms
Purpose: Legal terms for using Vorentix's services.
Key Sections: General Terms, Liabilities, Obligations, IP Rights, Governing Law, Termination.
9. FAQ
URL: /faq
Purpose: Provide answers to common questions about services and technologies.
Key Sections: Starting with Vorentix, Security, Access, Pricing.
10. Services
URL: /services
Purpose: Comprehensive overview of all Vorentix’s services.
Key Sections: Each service detailed in sub-pages, emphasizing features and integration capabilities.
All services will have an inner page also.
11. Contact
URL: /contact or /get-in-touch
Purpose: Facilitate communication for clients and partners.
Key Sections: Contact Form, Collaboration Invites, Link to Official Site.
Deliverables:
A fully responsive website design compatible with all devices and browsers.
Design files in Adobe XD or Sketch format.
Interactive prototypes where necessary.
https://files.brisdocs.example/doc/7QwkP2LmZ9xRt4VbNc8HsJy3FgDa6TeUoK1iWq5nBz_R/edit?tab=t.k8vn2pq4rtw#heading=h.zq7wd4xbfjm2
Updates
https://files.brisdocs.example/doc/7QwkP2LmZ9xRt4VbNc8HsJy3FgDa6TeUoK1iWq5nBz_R/edit?tab=t.h5m7cc19ptxe
Industry/Entity Type
Artificial Intelligence
Number of Pages Required
5+ page
Font styles to use
Other font styles liked:
- montserrat font
Requirements
Must have
- A prominent section about partnership, AI, and Child companies
Nice to have
- Follow the structure i have given in document https://files.brisdocs.example/doc/7QwkP2LmZ9xRt4VbNc8HsJy3FgDa6TeUoK1iWq5nBz_R/edit?tab=t.k8vn2pq4rtw#heading=h.zq7wd4xbfjm2

```html
<!DOCTYPE html>
<html lang="en">
<head>
<meta charset="utf-8">
<title>Vorentix Guides</title>
<link href="https://fonts.googleapis.com/css2?family=Montserrat:wght@400;500;600;700;800&display=swap" rel="stylesheet">
<style>
:root{
  --sky:#18DEFF;
  --cerulean:#52B8FF;
  --lavender:#B07CFF;
  --white:#FFFFFF;
  --black:#000000;
  --card:#1E0B52;
  --deep:#0A2742;
}
*{box-sizing:border-box;margin:0;padding:0}
html,body{width:1200px;height:4688px;overflow:hidden;background:var(--black);color:var(--white);font-family:'Montserrat',sans-serif}
a{color:inherit;text-decoration:none}
.page{position:relative;width:1200px;height:4688px}

/* header */
.site-header{position:absolute;top:0;left:0;width:1200px;height:120px}
.brand{position:absolute;left:64px;top:46px;display:flex;align-items:center;gap:10px}
.brand-dot{width:12px;height:12px;border-radius:50%;background:var(--cerulean)}
.brand-name{font-weight:500;font-size:26px;line-height:32px;letter-spacing:1px}
.main-nav{position:absolute;left:355px;top:56px;display:flex;gap:40px;font-size:13px;font-weight:500;text-transform:uppercase}
.main-nav .active{border-bottom:3px solid var(--lavender);padding-bottom:5px}
.btn{display:inline-flex;align-items:center;justify-content:center;background:linear-gradient(90deg,var(--sky),var(--lavender));border:2px solid var(--white);border-radius:6px;color:var(--white);font-weight:700;text-transform:uppercase}
.btn-header{position:absolute;left:962px;top:42px;width:170px;height:40px;font-size:13px}

/* hero */
.hero{position:absolute;top:0;left:0;width:1200px;height:672px}
.hero-visual{position:absolute;left:680px;top:170px;width:520px;height:400px;border-radius:50%;background:radial-gradient(ellipse at 50% 45%,#3aa0ff 0%,#1c3ea8 25%,#3a1266 45%,rgba(0,0,0,0) 70%)}
.hero-title{position:absolute;left:91px;top:215px}
.hero-title .l1{display:block;font-size:41px;font-weight:700;line-height:50px}
.hero-title .l2{display:block;font-size:30px;font-weight:700;line-height:40px}
.hl-lav{color:var(--lavender)}
.hl-sky{color:var(--sky)}
.hero-text{position:absolute;left:91px;top:334px;width:620px;font-size:19px;line-height:25px}
.btn-hero{position:absolute;left:91px;top:482px;width:250px;height:46px;font-size:13px}

/* featured */
.featured{position:absolute;top:672px;left:0;width:1200px;height:2303px;background:radial-gradient(ellipse at 90% 30%,#1a4f8a 0%,rgba(10,39,66,0) 45%),linear-gradient(180deg,#071a2e 0%,#0b2f4d 45%,#0d3a5e 80%,#0b2c4a 100%)}
.circuit-band{position:absolute;left:0;width:1200px;background:linear-gradient(180deg,rgba(24,222,255,0) 0%,rgba(82,184,255,.35) 60%,rgba(24,222,255,.15) 100%)}
.circuit-top{top:0;height:420px;opacity:.5}
.circuit-bottom{bottom:0;height:520px}
.section-title{font-size:36px;font-weight:700;text-align:center;text-transform:uppercase}
.featured .section-title{position:absolute;top:172px;width:1200px}
.featured-intro{position:absolute;top:246px;width:1200px;text-align:center;font-size:19px;line-height:25px}
.guide-card{position:absolute;width:466px;height:696px;background:var(--card);border:2px solid var(--lavender);border-radius:10px;text-align:center}
.guide-card h3{margin-top:42px;font-size:29px;font-weight:700;line-height:36px}
.guide-card p{margin:14px auto 0;width:420px;font-size:14px;line-height:21px}
.guide-media{position:absolute;left:38px;top:228px;width:382px;height:326px;border:3px solid var(--sky)}
.btn-card{position:absolute;left:152px;top:590px;width:160px;height:48px;font-size:13px;border-radius:8px}
.c1{left:93px;top:472px}.c2{left:659px;top:472px}
.c3{left:93px;top:1321px}.c4{left:659px;top:1321px}

/* future */
.future{position:absolute;top:2975px;left:0;width:1200px;height:583px;background:var(--black)}
.future .section-title{position:absolute;top:148px;width:1200px}
.future-list{position:absolute;top:242px;left:308px;list-style:none;font-size:20px;font-weight:700;color:var(--sky);line-height:24.4px}
.future-list li::before{content:"•";margin-right:14px}

/* subscribe */
.subscribe{position:absolute;top:3558px;left:0;width:1200px;height:457px;background:linear-gradient(90deg,var(--sky) 0%,#7fa8ff 45%,var(--lavender) 100%);text-align:center}
.subscribe h2{position:absolute;top:112px;width:1200px;font-size:36px;font-weight:700;text-transform:uppercase}
.subscribe p{position:absolute;top:158px;width:1200px;font-size:24px;line-height:30px;font-weight:500}
.email-field{position:absolute;left:262px;top:264px;width:464px;height:66px;border:2px solid var(--white);border-radius:6px;padding-left:24px;display:flex;align-items:center;font-size:18px;font-weight:600;background:rgba(255,255,255,.05)}
.btn-subscribe{position:absolute;left:744px;top:264px;width:194px;height:66px;font-size:17px}

/* footer */
.site-footer{position:absolute;top:4015px;left:0;width:1200px;height:673px;background:var(--black)}
.footer-brand{position:absolute;left:90px;top:94px;display:flex;align-items:center;gap:10px}
.store-badges{position:absolute;left:802px;top:96px;display:flex;gap:26px}
.store-badge{width:86px;height:28px;border:1px solid #888;border-radius:5px;background:#111}
.footer-col{position:absolute;top:230px;width:240px}
.footer-col h4{font-size:16px;font-weight:600;color:var(--sky);margin-bottom:22px}
.footer-col li{list-style:none;font-size:12px;line-height:35px}
.f1{left:88px}.f2{left:350px}.f3{left:612px}.f4{left:875px}
.social{display:flex;gap:14px;margin-top:14px}
.social span{width:32px;height:32px;border-radius:50%;background:var(--white)}
.copyright{position:absolute;top:580px;width:1200px;text-align:center;font-size:13px;line-height:34px}
</style>
</head>
<body>
<div class="page">

  <section class="hero">
    <div class="hero-visual" role="img" aria-label="Glowing blue circuit-board processor illustration"></div>
    <h1 class="hero-title">
      <span class="l1">EXPLORE, LEARN &amp; MASTER</span>
      <span class="l2">THE <span class="hl-lav">FUTURE</span> OF <span class="hl-sky">DIGITAL INNOVATION</span></span>
    </h1>
    <p class="hero-text">Welcome to Vorentix Guides — your go-to resource for expert knowledge, insights, and tutorials on Metaverse, Blockchain, Web3 and more. Whether you’re just starting or seeking advanced guidance, we’re here to empower your digital journey.</p>
    <a class="btn btn-hero" href="/build-an-avatar">Start Building My Avatar</a>
  </section>

  <header class="site-header">
    <a class="brand" href="/"><span class="brand-dot"></span><span class="brand-name">VORENTIX</span></a>
    <nav class="main-nav">
      <a href="/">Home</a><a href="/about">About</a><a class="active" href="/vorentix-guides">Vorentix Guides</a><a href="/services">Services</a><a href="/faq">FAQ</a><a href="/contact">Contact</a>
    </nav>
    <a class="btn btn-header" href="/build-an-avatar">Build an Avatar</a>
  </header>

  <section class="featured">
    <div class="circuit-band circuit-top" role="img" aria-label="Faint glowing circuit pattern"></div>
    <div class="circuit-band circuit-bottom" role="img" aria-label="Glowing cyan circuit-line pattern"></div>
    <h2 class="section-title">Featured Guides</h2>
    <p class="featured-intro">Explore the visionary projects where innovation meets experience<br>— from metaverse real estate to AI-powered avatars,<br>these creations showcase the future we’re building.</p>

    <article class="guide-card c1">
      <h3>Beguiners’ Guide<br>to the Metaverse</h3>
      <p>Undestand the basics of the metaverse,<br>its potential, and how to enter and<br>Thrive in this evolving digital universe.</p>
      <div class="guide-media" role="img" aria-label="Figure standing in a neon purple virtual portal room" style="background:linear-gradient(135deg,#3b1a9e,#b04dff 55%,#5a2bd6)"></div>
      <a class="btn btn-card" href="#">Read More</a>
    </article>

    <article class="guide-card c2">
      <h3>Dubai Real Estate<br>Tokenization Explained</h3>
      <p>Dive into the world of real state tokenization<br>in Dubai — learn how blockchain is transforming<br>property investment, ownership, and management.</p>
      <div class="guide-media" role="img" aria-label="Neon city skyline reflected on water at night" style="background:linear-gradient(180deg,#0b1440,#243d8f 50%,#0e2f6b 75%,#08173a)"></div>
      <a class="btn btn-card" href="#">Read More</a>
    </article>

    <article class="guide-card c3">
      <h3>Setting Up a<br>Crypto Wallet</h3>
      <p>Step-by[step guidance on how to securely<br>Set up and manage your cryptocurrency<br>Wallet, protecting your digital assets.</p>
      <div class="guide-media" role="img" aria-label="Digital wallet surrounded by glowing coins" style="background:linear-gradient(135deg,#1a2f6e,#3a6fb8 45%,#6a2e9e 80%,#2a1458)"></div>
      <a class="btn btn-card" href="#">Read More</a>
    </article>

    <article class="guide-card c4">
      <h3>Metaverse Integration &amp;<br>3D Space Development</h3>
      <p>Discover best practices for seamless metaverse<br>integration, including the essentials of<br>designing immersive, interactive 3D spaces.</p>
      <div class="guide-media" role="img" aria-label="Person wearing a VR headset in a neon city" style="background:linear-gradient(135deg,#2a6bd6,#6a3ac4 45%,#d03a8e 80%,#3a1660)"></div>
      <a class="btn btn-card" href="#">Read More</a>
    </article>
  </section>

  <section class="future">
    <h2 class="section-title">Future Guides</h2>
    <ul class="future-list">
      <li>Blockchain for Business: Real-world Use Cases</li>
      <li>Introduction to NFTs: Creation, Ownership &amp; Trading</li>
      <li>Smart Contracts Explained: The Essentials</li>
      <li>AI Integration in Blockchain &amp; Web3</li>
      <li>IoT &amp; Blockchain: Unlocking Smart Technologies</li>
      <li>How to Create Custom 3D Avatars</li>
      <li>AR, VR, MR: The Future of Immersive Experiences</li>
    </ul>
  </section>

  <section class="subscribe">
    <h2>Stay Ahead in the Digital World</h2>
    <p>Subscribe to Vorentix Guides for ongoing insights, experts tips,<br>And latest trends directly to our inbox.</p>
    <div class="email-field">Email</div>
    <a class="btn btn-subscribe" href="#">Subscribe</a>
  </section>

  <footer class="site-footer">
    <a class="footer-brand" href="/"><span class="brand-dot"></span><span class="brand-name">VORENTIX</span></a>
    <div class="store-badges">
      <span class="store-badge"></span><span class="store-badge"></span><span class="store-badge"></span>
    </div>
    <div class="footer-col f1"><h4>About Vorentix</h4><ul><li>About US</li><li>Our team</li><li>Vorentix Guides</li><li>Case Studies</li></ul></div>
    <div class="footer-col f2"><h4>Services</h4><ul><li>Metaverse Development</li><li>Blockchain Solutions</li><li>Crypto Wallets</li><li>AI Integration</li><li>Coin &amp; Token Development</li><li style="margin-top:6px">All Services</li></ul></div>
    <div class="footer-col f3"><h4>Resources</h4><ul><li>FAQ</li><li>Community Rules</li><li>Privacy Policy</li><li>Terms of Use</li><li>Support Center</li></ul></div>
    <div class="footer-col f4"><h4>Contact &amp; Connect</h4><ul><li>Contact Us</li><li>Email: info@vorentixgroup.com</li><li>Phone: + 1 (Phone Number)</li><li>Address: Business Address</li></ul>
      <div class="social"><span></span><span></span><span></span><span></span><span></span></div>
    </div>
    <p class="copyright">© 2025 Vorentix Group, Inc. All Rights Reserved.<br>Website: www.vorentixgroup.com</p>
  </footer>

</div>
</body>
</html>
```